Electrical Contracting business card design

We need a simple business card design for an Electrical Contracting business. A simple design would be appreciated
This company has 2 directors so on one it would have Colin Marsh & another with Dana Marsh.
Updates

Reason: Hello A few designers have asked for a logo unfortunately we don't have one so have extended deadline to see who can help us out with this. CHEERS

Reason: Waiting for business partner to return from xmas break. cheers

Industry/Entity Type

Business

Contact Information for Business Card

Volmera Electrical Services P/L
REC: 36074
Residential Commercial Industrial
Service-Repairs-Renovations-Installations-Telephone-Data
Colin Marsh-Ph: 0433 517 862
Email: colin@volmeraelectrical.com.au

Requirements
Should not have
• The design should not have any electrical appliances in it ie: power-points, leads, houses etc.

```html
<!DOCTYPE html>
<html lang="en">
<head>
<meta charset="utf-8">
<title>Volmera Electrical Services – Business Card</title>
<link href="https://fonts.googleapis.com/css2?family=Carlito:wght@400;700&display=swap" rel="stylesheet">
<style>
  :root {
    --brand-red: #a31b22;
    --brand-red-soft: #c9787b;
    --card-white: #ffffff;
    --text-light: #ffffff;
    --backdrop: #e8e3da;
  }
  * { margin: 0; padding: 0; box-sizing: border-box; }
  html, body {
    width: 1200px;
    height: 1062px;
    overflow: hidden;
    background: var(--backdrop);
    font-family: "Carlito", "Calibri", sans-serif;
  }
  .canvas {
    position: relative;
    width: 1200px;
    height: 1062px;
  }
  .card {
    position: absolute;
    box-shadow: 0 2px 6px rgba(0,0,0,0.12);
  }

  /* Front */
  .card-front {
    left: 184px;
    top: 118px;
    width: 568px;
    height: 350px;
    background: var(--card-white);
    display: flex;
    align-items: center;
    justify-content: center;
  }
  .front-name {
    color: var(--brand-red);
    font-size: 34px;
    font-weight: 400;
    letter-spacing: 0.3px;
  }

  /* Back */
  .card-back {
    left: 441px;
    top: 545px;
    width: 570px;
    height: 351px;
    background: var(--card-white);
    overflow: hidden;
  }
  .back-panel {
    position: absolute;
    left: 0;
    top: 0;
    width: 570px;
    height: 273px;
    background: var(--brand-red);
  }
  .back-glow {
    position: absolute;
    left: 36px;
    top: 8px;
    width: 257px;
    height: 159px;
    background: linear-gradient(180deg, rgba(255,255,255,0.55) 0%, rgba(255,255,255,0.25) 35%, rgba(201,120,123,0.15) 75%, rgba(163,27,34,0) 100%);
  }
  .back-title {
    position: absolute;
    left: 47px;
    top: 23px;
    font-size: 19px;
    color: #5a1014;
  }
  .directors {
    position: absolute;
    left: 69px;
    top: 167px;
    color: var(--text-light);
    font-size: 19px;
    line-height: 30px;
  }
  .phone {
    position: absolute;
    left: 67px;
    top: 239px;
    color: var(--text-light);
    font-size: 19px;
  }
  .services {
    position: absolute;
    left: 395px;
    top: 64px;
    list-style: none;
    color: var(--text-light);
    font-size: 19px;
    line-height: 19.5px;
  }
  .contact-band {
    position: absolute;
    left: 0;
    top: 273px;
    width: 570px;
    height: 78px;
    text-align: center;
    color: var(--brand-red);
    font-size: 18px;
  }
  .licence { position: absolute; left: 0; right: 24px; top: 7px; }
  .email { position: absolute; left: 12px; right: 0; top: 38px; }
</style>
</head>
<body>
<main class="canvas">
  <section class="card card-front" aria-label="Business card front">
    <h1 class="front-name">Volmera Electrical Services</h1>
  </section>

  <section class="card card-back" aria-label="Business card back">
    <div class="back-panel">
      <div class="back-glow" role="img" aria-label="Soft light-streak decoration behind the company name"></div>
      <p class="back-title">Volmera Electrical Services</p>
      <ul class="services">
        <li>Repairs</li>
        <li>Renovations</li>
        <li>Installations</li>
        <li>Telephone</li>
        <li>Data</li>
      </ul>
      <div class="directors">
        <p>Colin Marsh</p>
        <p>Dana Marsh</p>
      </div>
      <p class="phone">Ph: 0433 517 862</p>
    </div>
    <div class="contact-band">
      <p class="licence">P/L REC: 36074 Residential Commercial Industrial Service</p>
      <p class="email">Email: colin@volmeraelectrical.com.au</p>
    </div>
  </section>
</main>
</body>
</html>
```